Etiketten-Design für Produkte eines Familienbetriebs mit Imkerei und Hühnerhaltung
Zielgruppe
Wir sind ein Familienbetrieb mit Imkerei und Hühnerhaltung. Wir suchen für unsere Produkte ein modernes Corporate Design, mit zentralen, bei jedem Produkt vorkommenden Elementen, sowie Elementen, welche produktindividuell sind.
Wir leben in einem 150 jährigen Riegelhaus, welches in der Umgebung sehr bekannt ist. Es soll im Etiketten-Design zentral erscheinen.
Unsere Produkte sind: Honig, Pollen, Eier
Aufgabenstellung
1. Zentrale, auf allen Etiketten wiederkehrende Elemente:
- Unser Riegelhaus (stilisiert) (Bild beiliegend)
- Das Wort 'Birkeneck' (Anmerkung: ohne Anführungszeichen)
- die zentralen Elemente sollen die Produkte nicht überragen.
2. Dezente Adresse:
- Familie Dorbach, Birkeneck, CH-9573 Holtikon
3. Produkte:
a) Honig
Sorten: Waldhonig (dunkel), Blütenhonig (gelblich-goldig), Crèmehonig (gelblich-weisslich), Lavendelhonig (gelblich-goldig)
Die Honigsorten sollen farblich hervortreten.
Freifeld (zweizeilig): für die Lotnummer und die Haltbarkeitsangabe)
Gewicht: 250 g, 500 g
b) Pollen
Gewicht: 100 g
c) Eier
Verpackungseinheiten: 4er-, 6er-, 10er-Packung
Haltungsform: BIO-Haltung
das Wort 'frisch'
Farbe grün (=Bio) soll farblich hervortreten (ähnlich wie beim Honig)
Freifeld (zweizeilig: für das Eigewicht und die Haltbarkeitsangabe)
Bitte keine Stock-Bilder verwenden. Die Etiketten sollen schlicht, edel ,schörkellos und modern erscheinen.
Das Etikett soll Exklusivität und Qualität ausstrahlen. Etikettenhintergrund einfarbig.
Interessanterweise gibt es bei Weinen solche Etiketten. Ich habe einige rausgesucht und angehängt, um die Richtung vorzugeben. (Wein1-6)
Ich habe auch eine schlichte Honigetikette gefunden, die ins Schema passt. (Imker1)
Zusätzlich sind jetzt auch noch Farbbeispiele der Honigsorten zur besseren Abstimmung von Inhalt und Etikette beigelegt. Lavendelhonig ist dem Blütenhonig sehr ähnlich.
Etikettengrössen:
Honig/Pollen 250 g: 190 x 42 mm
Honig 500 g: 206 x 45 mm
Eier 4er: 60 x 60 mm
Eier 6er: 110 x 60 mm
Eier 10er: 170 x 60 cm

```html
<!DOCTYPE html>
<html lang="de">
<head>
<meta charset="utf-8">
<title>Birkeneck Honig – Etiketten</title>
<link rel="stylesheet" href="https://fonts.googleapis.com/css2?family=Crimson+Pro:wght@400;500;600;700&display=swap">
<style>
  :root {
    --page: #ffffff;
    --label: #1d1d1d;
    --label-texture: #262626;
    --text-grey: #a7a7a7;
    --lavendel: #9a4f95;
    --blueten: #e8830f;
    --wald: #5b8a23;
    --creme: #f7d898;
  }
  * { margin: 0; padding: 0; box-sizing: border-box; }
  html, body {
    width: 1200px;
    height: 519px;
    overflow: hidden;
    background: var(--page);
  }
  .label-set {
    position: relative;
    width: 1200px;
    height: 519px;
    font-family: "Crimson Pro", Georgia, serif;
  }
  .honey-label {
    position: absolute;
    top: 87px;
    width: 270px;
    height: 283px;
  }
  .honey-label--lavendel { left: 18px; top: 90px; }
  .honey-label--blueten { left: 317px; }
  .honey-label--wald { left: 619px; }
  .honey-label--creme { left: 922px; }

  .seal-strip {
    position: absolute;
    left: 50%;
    transform: translateX(-50%);
    top: 0;
    width: 41px;
    height: 104px;
    background: var(--label);
  }
  .label-body {
    position: absolute;
    left: 0;
    top: 103px;
    width: 270px;
    height: 180px;
    background: var(--label);
    color: var(--text-grey);
  }
  .texture {
    position: absolute;
    inset: 0;
    background: radial-gradient(ellipse at center, var(--label-texture), var(--label) 80%);
  }
  .brand-mark {
    position: absolute;
    left: 50%;
    top: 10px;
    width: 22px;
    height: 22px;
    margin-left: -11px;
    border-radius: 50%;
    background: var(--text-grey);
  }
  .brand-name {
    position: absolute;
    left: 0;
    right: 0;
    top: 34px;
    text-align: center;
    font-size: 29px;
    font-weight: 400;
    font-variant: small-caps;
    letter-spacing: 0.5px;
    line-height: 1;
  }
  .variety {
    position: absolute;
    left: 0;
    right: 0;
    top: 62px;
    display: flex;
    justify-content: center;
    white-space: nowrap;
    font-size: 68px;
    font-weight: 600;
    line-height: 1;
  }
  .variety span {
    display: inline-block;
    transform: scaleX(0.64);
    transform-origin: center;
  }
  .honey-label--lavendel .variety { color: var(--lavendel); }
  .honey-label--blueten .variety { color: var(--blueten); }
  .honey-label--wald .variety { color: var(--wald); }
  .honey-label--creme .variety { color: var(--creme); }
  .product-type {
    position: absolute;
    left: 0;
    right: 0;
    top: 120px;
    display: flex;
    justify-content: center;
    font-size: 36px;
    font-weight: 500;
    line-height: 1;
  }
  .product-type span {
    display: inline-block;
    transform: scaleX(0.72);
  }
  .weight {
    position: absolute;
    right: 26px;
    bottom: 12px;
    font-size: 25px;
    font-weight: 400;
    line-height: 1;
  }
</style>
</head>
<body>
<main class="label-set">
  <article class="honey-label honey-label--lavendel">
    <div class="seal-strip"></div>
    <div class="label-body">
      <div class="texture" role="img" aria-label="Dezentes dunkles Sonnenspiralen-Muster"></div>
      <span class="brand-mark"></span>
      <p class="brand-name">Birkeneck</p>
      <h2 class="variety"><span>LAVENDEL</span></h2>
      <p class="product-type"><span>HONIG</span></p>
      <p class="weight">250g</p>
    </div>
  </article>
  <article class="honey-label honey-label--blueten">
    <div class="seal-strip"></div>
    <div class="label-body">
      <div class="texture" role="img" aria-label="Dezentes dunkles Sonnenspiralen-Muster"></div>
      <span class="brand-mark"></span>
      <p class="brand-name">Birkeneck</p>
      <h2 class="variety"><span>BLÜTEN</span></h2>
      <p class="product-type"><span>HONIG</span></p>
      <p class="weight">250g</p>
    </div>
  </article>
  <article class="honey-label honey-label--wald">
    <div class="seal-strip"></div>
    <div class="label-body">
      <div class="texture" role="img" aria-label="Dezentes dunkles Sonnenspiralen-Muster"></div>
      <span class="brand-mark"></span>
      <p class="brand-name">Birkeneck</p>
      <h2 class="variety"><span>WALD</span></h2>
      <p class="product-type"><span>HONIG</span></p>
      <p class="weight">250g</p>
    </div>
  </article>
  <article class="honey-label honey-label--creme">
    <div class="seal-strip"></div>
    <div class="label-body">
      <div class="texture" role="img" aria-label="Dezentes dunkles Sonnenspiralen-Muster"></div>
      <span class="brand-mark"></span>
      <p class="brand-name">Birkeneck</p>
      <h2 class="variety"><span>CRÈME</span></h2>
      <p class="product-type"><span>HONIG</span></p>
      <p class="weight">250g</p>
    </div>
  </article>
</main>
</body>
</html>
```